Courier Business needs a Business Card Design !!!

My new company needs a business card design. Our company name is Maple Dart Courier & Delivery Services. We will be servicing residential , government and business clients in the City of Yellowknife, Northwest Territories, Canada. I would like the following information included on the card: Name- Calvin Oxley. Title- Owner. Company- Maple Dart Courier & Delivery Services. Address- PO Box 5918 , Yellowknife , NWT, X0E 4K3. Phone- 867-555-0193. Email- mapledartdelivery@postfern.example. Facebook- www.socialpage.example/mapledartdelivery. I would like my double sided card to be the standard size of 84mm x 55mm. No borders. Use CMYK mode.1039x 697 pixels at least. I would like my logo to take up at least one quarter of the area of one side of the card. Text should be at least 8 point with perhaps my name being 10 point and my company name being 12-15 point . It should have clear readable font. Please use one or two bold colors. I am trying to attract the business community so a professional look might be best. My tag line is " On Time Every Time ". Nice safe margins please. We will be providing fast, reliable and professional delivery of envelopes and small packages within the City of Yellowknife. We offer 100% satisfaction or a complete refund. I have included a file of our logo. I like black, blue and red but am willing to look at what you feel would work best. I do not really like white as a background color.

Target Market(s)

Professionals , business owners. 30-50 years old

Industry/Entity Type

Residential

Contact Information for Business Card

As noted in brief

Font styles to use
Serif
Sans Serif

Colors
000000
0255a3
f04a50

Requirements
Must have
• My contact info. My logo
Nice to have
• Simple elegant design but still catches the eye
Should not have
• White background color

```html
<!DOCTYPE html>
<html lang="en">
<head>
<meta charset="utf-8">
<title>Maple Dart Courier &amp; Delivery Services – Business Card</title>
<link rel="stylesheet" href="https://fonts.googleapis.com/css2?family=Cinzel:wght@400;600;700&family=Montserrat:wght@500;700;800&display=swap">
<style>
  :root {
    --backdrop: #e7e4df;
    --card-dark: #2f2f31;
    --pattern-dark: #373739;
    --card-grey: #9c9c9c;
    --ink: #111111;
    --ink-light: #f1f1f1;
    --brand-red: #f04a50;
    --brand-blue: #0255a3;
    --brand-lime: #b7d43a;
    --frame-purple: #8a4fb0;
  }
  * { box-sizing: border-box; margin: 0; padding: 0; }
  html, body {
    width: 1200px; height: 800px; overflow: hidden;
    background: var(--backdrop);
  }
  .sheet { position: relative; width: 1200px; height: 800px; }
  .card {
    position: absolute; top: 223px;
    width: 540px; height: 354px;
    border-radius: 14px; overflow: hidden;
    box-shadow: 0 6px 18px rgba(0,0,0,.18);
  }
  .card--front { left: 40px; background: var(--card-dark); }
  .card--back  { left: 620px; background: var(--card-dark); }

  .card__pattern { position: absolute; inset: 0; }
  .card__frame { position: absolute; inset: 0; pointer-events: none; }

  /* Front */
  .front__wordmark {
    position: absolute; left: 60px; right: 60px; top: 118px;
    text-align: center;
    font-family: "Montserrat", sans-serif; font-weight: 800;
    font-size: 20px; line-height: 1.2; letter-spacing: .3px;
    text-transform: uppercase; color: var(--brand-lime);
  }
  .front__wordmark-name { display: block; font-size: 28px; }
  .front__tagline {
    position: absolute; left: 30px; right: 30px; bottom: 52px;
    text-align: center;
    font-family: "Cinzel", serif; font-weight: 600;
    font-size: 15px; letter-spacing: 1.4px;
    color: var(--ink-light);
  }

  /* Back */
  .back__panel { position: absolute; inset: 0; }
  .back__wordmark {
    position: absolute; left: 0; right: 0; top: 30px;
    text-align: center;
    font-family: "Montserrat", sans-serif; font-weight: 800;
    font-size: 14px; line-height: 1.15; text-transform: uppercase;
    color: #3a3a3a;
  }
  .back__identity {
    position: absolute; left: 50px; top: 118px; width: 212px;
    font-family: "Cinzel", serif; color: var(--ink);
  }
  .back__name { font-size: 22px; font-weight: 600; letter-spacing: .5px; }
  .back__title { font-size: 14px; font-weight: 600; text-align: right; margin-top: 2px; }
  .back__divider {
    position: absolute; left: 282px; top: 92px; width: 2px; height: 104px;
    background: linear-gradient(var(--brand-blue), var(--frame-purple));
  }
  .contact {
    position: absolute; left: 306px;
    font-family: "Montserrat", sans-serif; font-weight: 500;
    font-size: 12.5px; line-height: 1.55; letter-spacing: .4px;
    display: flex; gap: 10px; align-items: flex-start;
  }
  .contact--address { top: 100px; color: #1b1b1b; text-transform: uppercase; font-style: normal; }
  .contact--phone { top: 178px; color: #1b1b1b; }
  .contact--email { top: 254px; left: 70px; color: var(--ink-light); font-size: 12px; }
  .contact--social { top: 290px; left: 70px; color: var(--ink-light); font-size: 12px; }
  .contact__icon { flex: 0 0 14px; width: 14px; height: 14px; margin-top: 2px; }
</style>
</head>
<body>
<main class="sheet">

  <section class="card card--front" aria-label="Card front">
    <svg class="card__pattern" width="540" height="354" role="img" aria-label="Faint repeating bird silhouette pattern">
      <rect width="540" height="354" fill="var(--pattern-dark)" opacity=".55"/>
    </svg>
    <svg class="card__frame" width="540" height="354">
      <defs>
        <linearGradient id="frontFrame" x1="0" y1="0" x2="0" y2="1">
          <stop offset="0" stop-color="var(--brand-red)"/>
          <stop offset=".5" stop-color="var(--frame-purple)"/>
          <stop offset="1" stop-color="var(--brand-blue)"/>
        </linearGradient>
      </defs>
      <rect x="12" y="12" width="516" height="330" rx="12" fill="none" stroke="url(#frontFrame)" stroke-width="1.5"/>
    </svg>
    <h1 class="front__wordmark"><span class="front__wordmark-name">Maple Dart</span>Courier &amp; Delivery Services</h1>
    <p class="front__tagline">Fast, Reliable and Professional Delivery</p>
  </section>

  <section class="card card--back" aria-label="Card back">
    <svg class="back__panel" width="540" height="354">
      <defs>
        <linearGradient id="seamLine" x1="0" y1="0" x2="1" y2="0">
          <stop offset="0" stop-color="var(--brand-red)"/>
          <stop offset=".6" stop-color="var(--frame-purple)"/>
          <stop offset="1" stop-color="var(--brand-blue)"/>
        </linearGradient>
        <linearGradient id="backFrame" x1="0" y1="0" x2="0" y2="1">
          <stop offset="0" stop-color="var(--brand-red)"/>
          <stop offset="1" stop-color="var(--brand-blue)"/>
        </linearGradient>
      </defs>
      <rect width="540" height="354" fill="var(--card-dark)"/>
      <rect y="220" width="540" height="134" fill="var(--pattern-dark)" opacity=".55" role="img" aria-label="Faint repeating bird silhouette pattern"/>
      <path d="M0 0 H540 V206 Q400 214 290 234 Q150 240 0 240 Z" fill="var(--card-grey)"/>
      <path d="M150 240 Q290 236 400 214 Q470 206 540 206" fill="none" stroke="url(#seamLine)" stroke-width="2"/>
      <rect x="12" y="12" width="516" height="330" rx="12" fill="none" stroke="url(#backFrame)" stroke-width="1.5"/>
    </svg>

    <h2 class="back__wordmark">Maple Dart<br>Courier &amp; Delivery Services</h2>

    <div class="back__identity">
      <p class="back__name">Calvin Oxley</p>
      <p class="back__title">Proprietor</p>
    </div>
    <div class="back__divider"></div>

    <address class="contact contact--address">
      <svg class="contact__icon" viewBox="0 0 14 14" aria-hidden="true">
        <path d="M7 1a4 4 0 0 1 4 4c0 3-4 8-4 8S3 8 3 5a4 4 0 0 1 4-4z" fill="var(--brand-lime)"/>
        <circle cx="7" cy="5" r="1.5" fill="var(--card-grey)"/>
      </svg>
      <span>PO Box 5918<br>Yellowknife NWT<br>X0E 4K3</span>
    </address>

    <p class="contact contact--phone">
      <svg class="contact__icon" viewBox="0 0 14 14" aria-hidden="true">
        <path d="M3 1.5l2.2 2.6-1.2 1.4a8 8 0 0 0 4.5 4.5l1.4-1.2 2.6 2.2-1.3 1.6C6.5 12.6 1.4 7.5 1.4 2.8z" fill="#1b1b1b"/>
      </svg>
      <span>867-555-0193</span>
    </p>

    <p class="contact contact--email">
      <svg class="contact__icon" viewBox="0 0 14 14" aria-hidden="true">
        <rect x="1" y="3" width="12" height="8.5" rx="1" fill="none" stroke="var(--ink-light)" stroke-width="1.2"/>
        <path d="M1.5 3.5 7 8l5.5-4.5" fill="none" stroke="var(--ink-light)" stroke-width="1.2"/>
      </svg>
      <span>mapledartdelivery@postfern.example</span>
    </p>

    <p class="contact contact--social">
      <svg class="contact__icon" viewBox="0 0 14 14" aria-hidden="true">
        <circle cx="7" cy="7" r="6" fill="var(--brand-blue)"/>
      </svg>
      <span>www.socialpage.example/mapledartdelivery</span>
    </p>
  </section>

</main>
</body>
</html>
```